Business Card Design Project

Hi Designers, this project is currently on hold until the Logo is completed:
Please submit to the Logo project here:
http://work.pitchvault.example/brief.aspx?id=413907

Once logo is completed, it will be attached to this project for you to create business cards with show logo, company name and address

Maren T R Quillby

Osric's Tiny Grey Heron Co.
Fernbrook
Nether Coombsby
North Devon EX91 4TZ

Tel: 01809 417356
Mobile: 07900 263818
email: maren@tiny-grey-heron.example.co.uk

Project Deadline Extended
Reason: Sorry everyone, we have had a sick ewe and I am now behind with this one and need to extend the deadline. Best wishes Maren

The designer who wins the logo brief will be asked to design the business card. Many thanks Maren

Project Deadline Extended
Reason: Sorry everyone, just a chaotic time of year with animals. Need to extend the deadline again..... as I just haven't had enough time to take a good look.... Thank you for your understanding. Maren

Project Deadline Extended
Reason: Sorry everyone It is our busiest time of year with animals and just no time to spend going through such great designs. I will have to extend the deadline again and hopefully have some news very soon. Wishing you all a very happy Christmas and a happy and healthy new year. Maren & Osric

High end market
Boutique restaurants for meat (it's not commercial lamb it's a slow matured quality meat more like venison/beef) expensive - specialized market

High End shoot clothing / wool / sheepskin rugs
Quality products

Business

• based on the logo - (which Pitch Vault has just been asked to do)
possibly based on a simplified picture of a Hebridean Ram (shows it's a Hebridean by it's horns as opposed to other black sheep!!)

```html
<!DOCTYPE html>
<html lang="en">
<head>
<meta charset="utf-8">
<title>Osric's Tiny Grey Heron Co. – Business Cards</title>
<link href="https://fonts.googleapis.com/css2?family=Open+Sans:wght@400;600&display=swap" rel="stylesheet">
<style>
  :root {
    --page-bg: #e8e5e0;
    --card-dark: #2b3132;
    --card-dark-deep: #1f2425;
    --card-light: #f7f7f7;
    --card-light-edge: #dcdcdc;
    --stripe-grey: #9c9fa0;
    --ink-dark: #3a3f40;
    --ink-light: #f2f2f2;
  }
  * { box-sizing: border-box; margin: 0; padding: 0; }
  html, body {
    width: 1200px; height: 1023px; overflow: hidden;
    background: var(--page-bg);
    font-family: "Open Sans", Arial, sans-serif;
  }
  .card {
    position: absolute;
    width: 640px; height: 370px;
    border-radius: 4px;
    overflow: hidden;
    box-shadow: 0 8px 24px rgba(0,0,0,0.18);
  }
  .card-front { left: 280px; top: 95px; }
  .card-back {
    left: 280px; top: 545px;
    background: linear-gradient(135deg, var(--card-dark) 0%, var(--card-dark-deep) 100%);
  }
  .card-art { position: absolute; inset: 0; }

  .holder-name {
    position: absolute; right: 34px; top: 22px;
    font-size: 22px; color: var(--ink-dark);
    padding-bottom: 6px;
    border-bottom: 2px solid var(--ink-dark);
    padding-left: 10px;
  }
  .brand-mark {
    position: absolute; left: 36px; top: 96px;
    display: flex; align-items: center; gap: 12px;
  }
  .brand-dot {
    width: 38px; height: 38px; border-radius: 50%;
    background: var(--ink-dark);
  }
  .brand-name {
    font-size: 17px; font-weight: 600; color: var(--ink-dark);
    letter-spacing: 0.5px;
  }
  .address {
    position: absolute; left: 36px; top: 160px;
    font-size: 14px; line-height: 21px; color: var(--ink-dark);
    list-style: none;
  }
  .contact {
    position: absolute; left: 260px; top: 300px;
    font-size: 13px; line-height: 19px; color: var(--ink-light);
    list-style: none;
  }

  .back-mark {
    position: absolute; left: 0; right: 0; top: 0; bottom: 0;
    display: flex; align-items: center; justify-content: center; gap: 18px;
  }
  .back-dot {
    width: 64px; height: 64px; border-radius: 50%;
    border: 5px solid var(--ink-light);
  }
  .back-name {
    font-size: 26px; font-weight: 400; color: var(--ink-light);
    letter-spacing: 1px;
  }
</style>
</head>
<body>

<section class="card card-front" aria-label="Business card front">
  <svg class="card-art" width="640" height="370" viewBox="0 0 640 370" aria-hidden="true">
    <defs>
      <linearGradient id="front-light" x1="0" y1="0" x2="1" y2="1">
        <stop offset="0" stop-color="#ffffff"/>
        <stop offset="1" stop-color="#dcdcdc"/>
      </linearGradient>
      <linearGradient id="front-dark" x1="0" y1="0" x2="1" y2="1">
        <stop offset="0" stop-color="#343a3b"/>
        <stop offset="1" stop-color="#1f2425"/>
      </linearGradient>
    </defs>
    <rect width="640" height="370" fill="url(#front-light)"/>
    <path d="M640 60 C515 144 390 262 0 310 L0 324 C400 276 525 158 640 76 Z" fill="#9c9fa0"/>
    <path d="M640 84 C530 166 410 284 0 334 L0 370 L640 370 Z" fill="url(#front-dark)"/>
  </svg>

  <div class="holder-name">Maren T R Quillby</div>

  <div class="brand-mark">
    <span class="brand-dot"></span>
    <span class="brand-name">Osric's Tiny Grey Heron Co.</span>
  </div>

  <ul class="address">
    <li>Osric's Tiny Grey Heron Co.</li>
    <li>Fernbrook</li>
    <li>Nether Coombsby</li>
    <li>North Devon EX91 4TZ</li>
  </ul>

  <ul class="contact">
    <li>Tel: 01809 417356</li>
    <li>Mobile: 07900 263818</li>
    <li>email: maren@tiny-grey-heron.example.co.uk</li>
  </ul>
</section>

<section class="card card-back" aria-label="Business card back">
  <div class="back-mark">
    <span class="back-dot"></span>
    <span class="back-name">Osric's Tiny Grey Heron Co.</span>
  </div>
</section>

</body>
</html>
```